plovu business card design

plovu is an incubator within RTM Media focused on unlocking the potential in underserved niche micro-verticals on the web. our mission is to rapidly develop and foster emerging micro-verticals bc they are ripe for growth - building interesting and trusted content experiences with unqiue, useful and cutting-edge delivery methods.please do all copy (except for RTM Media, which must look as typed here and in logo) in all lowercase. Also please use spaces between phone # extensions not dashes or periods. I have attached all variations of the logo.
Industry/Entity Type
Business
Contact Information for Business Card
daria feltow, ceo www.plovu.io 218 holbrook lane 3rd floor oakland ca 94731 415 602 0002m 510 985 7966d daria.feltow@plovu.io
Look and feel
Each slider illustrates characteristics of the customer's brand and the style your logo design should communicate.

```html
<!DOCTYPE html>
<html lang="en">
<head>
<meta charset="utf-8">
<title>plovu business card</title>
<link rel="stylesheet" href="https://fonts.googleapis.com/css2?family=Nunito+Sans:wght@400;600;700;800&display=swap">
<style>
  :root {
    --page: #e6e8e9;
    --card: #f8f9f9;
    --card-edge: #d3d7d8;
    --ink: #1e1e1e;
    --teal: #2f5d58;
    --on-teal: #ffffff;
  }
  * { box-sizing: border-box; margin: 0; padding: 0; }
  html, body {
    width: 1200px;
    height: 970px;
    overflow: hidden;
    background: var(--page);
    font-family: "Nunito Sans", sans-serif;
    color: var(--ink);
  }
  .card {
    position: absolute;
    left: 100px;
    top: 207px;
    width: 1000px;
    height: 556px;
    background: var(--card);
    border: 1px solid var(--card-edge);
    overflow: hidden;
  }
  .brand {
    position: absolute;
    left: 50px;
    top: 34px;
    font-size: 120px;
    font-weight: 800;
    line-height: 1;
    letter-spacing: 2px;
    color: var(--ink);
  }
  .tagline {
    position: absolute;
    left: 52px;
    top: 186px;
    font-size: 25px;
    font-weight: 400;
  }
  .address {
    position: absolute;
    left: 50px;
    top: 270px;
    font-size: 26px;
    line-height: 33px;
  }
  .contacts {
    position: absolute;
    left: 50px;
    top: 362px;
    list-style: none;
    font-size: 26px;
  }
  .contacts li {
    display: flex;
    align-items: center;
    height: 40px;
  }
  .contact-icon {
    width: 30px;
    height: 30px;
    margin-right: 14px;
    flex: none;
  }
  .site-name { font-weight: 700; color: var(--teal); }
  .splash {
    position: absolute;
    right: 0;
    top: 0;
    width: 440px;
    height: 100%;
    background: var(--teal);
    border-radius: 180px 0 0 200px;
  }
  .person {
    position: absolute;
    left: 596px;
    top: 290px;
    color: var(--on-teal);
  }
  .person-name {
    font-size: 40px;
    font-weight: 700;
    line-height: 1.1;
  }
  .person-role {
    font-size: 26px;
    font-weight: 400;
  }
</style>
</head>
<body>
  <section class="card">
    <div class="splash" role="img" aria-label="Teal ink splatter decoration"></div>

    <div class="brand">plovu</div>
    <p class="tagline">an RTM Media incubator</p>

    <p class="address">218 Holbrook Lane 3rd floor<br>Oakland, CA 94731</p>

    <ul class="contacts">
      <li>
        <svg class="contact-icon" viewBox="0 0 30 30" aria-hidden="true">
          <circle cx="15" cy="15" r="15" fill="var(--teal)"/>
          <rect x="10.5" y="6.5" width="9" height="17" rx="1.5" fill="none" stroke="#fff" stroke-width="1.8"/>
          <circle cx="15" cy="20.5" r="1" fill="#fff"/>
        </svg>
        415 738 4196
      </li>
      <li>
        <svg class="contact-icon" viewBox="0 0 30 30" aria-hidden="true">
          <circle cx="15" cy="15" r="15" fill="var(--teal)"/>
          <path d="M7 12c0-3 16-3 16 0v2h-4v-2h-8v2H7z" fill="#fff"/>
          <rect x="9" y="15" width="12" height="7" rx="1.5" fill="#fff"/>
        </svg>
        510 247 3859
      </li>
      <li>
        <svg class="contact-icon" viewBox="0 0 30 30" aria-hidden="true">
          <circle cx="15" cy="15" r="15" fill="var(--teal)"/>
          <rect x="7.5" y="9.5" width="15" height="11" fill="none" stroke="#fff" stroke-width="1.8"/>
          <path d="M7.5 9.5l7.5 6 7.5-6" fill="none" stroke="#fff" stroke-width="1.8"/>
        </svg>
        daria.feltow@plovu.io
      </li>
      <li>
        <svg class="contact-icon" viewBox="0 0 30 30" aria-hidden="true">
          <circle cx="15" cy="15" r="15" fill="var(--teal)"/>
          <circle cx="15" cy="15" r="8" fill="none" stroke="#fff" stroke-width="1.8"/>
          <path d="M7 15h16M15 7c-4 5-4 11 0 16M15 7c4 5 4 11 0 16" fill="none" stroke="#fff" stroke-width="1.4"/>
        </svg>
        <span>www.<span class="site-name">plovu</span>.io</span>
      </li>
    </ul>

    <div class="person">
      <p class="person-name">Daria Feltow</p>
      <p class="person-role">CEO</p>
    </div>
  </section>
</body>
</html>
```